corVenna Bright Studio Website coded

New website (coded) promoting photography, videography and graphic design
Fresh, clean, crisp modern striking
easy to navigate
www.corvenna.com.au, current outdated site. Needs to be more streamlined.
Check out www.facebook.com/corVenna.Snaps
Offering the following photography categories
Family portraiture
Lifestyle photography (celebrations)
Pets
Fine Art
Arts and Sports .. I.e. Bands, schools, teams, performances, etc)
Commercial
Additional Services
Design
Photo books
Photo restoration
Videography and editing
Then there should be a bio, testimonial, where I am located, FAQ, pricing info perhaps all under the one umbrella of About Me or INFO
I also need a client log-in area to sell my photography, i.e. a plug-in. I am currently using pictavault for this.

```html
<!DOCTYPE html>
<html lang="en">
<head>
<meta charset="utf-8">
<title>corVenna Bright Studio — Portrait Photographer Sydney</title>
<link rel="stylesheet" href="https://fonts.googleapis.com/css2?family=Questrial&display=swap">
<style>
:root{
  --black:#000;
  --paper:#ececec;
  --lime:#b1cf3a;
  --orange:#f58f50;
  --ink:#3c3c3c;
  --muted:#5a5a5a;
  --dim:#333;
  --white:#fff;
  --tab:#3a3a3a;
}
*{margin:0;padding:0;box-sizing:border-box}
html,body{width:1200px;height:1199px;overflow:hidden}
body{background:var(--paper);font-family:"Questrial",sans-serif;color:var(--ink);position:relative}
.abs{position:absolute}
.masthead{left:0;top:0;width:1200px;height:319px;background:var(--black)}
.lens{left:252px;top:24px;width:205px;height:168px;border-radius:50%;
  background:radial-gradient(circle at 55% 50%,#6a2a6e 0,#2a1630 18%,#141414 40%,#000 70%)}
.logo{left:252px;top:46px;font-size:26px;color:var(--white);letter-spacing:.5px}
.nav{left:550px;top:0;display:flex;height:72px}
.nav a{color:var(--white);text-decoration:none;font-size:10.5px;line-height:104px;height:72px;display:block}
.nav .current{background:var(--lime);width:50px;text-align:center}
.nav a.s{margin-left:7px}
.nav a.a{margin-left:53px}
.nav a.t{margin-left:21px}
.nav a.f{margin-left:43px}
.nav a.c{margin-left:21px}
.tagline{left:0;width:1152px;top:104px;text-align:center;font-size:21px;line-height:24px;color:#5d5d5d;text-transform:uppercase}
.photo{background:linear-gradient(135deg,#9a9a9a,#d4d4d4 50%,#6d6d6d)}
.side-left{left:251px;top:212px;width:110px;height:195px}
.side-right{left:778px;top:212px;width:128px;height:195px}
.slide{left:361px;top:168px;width:417px;height:280px;border:3px solid var(--white);overflow:hidden}
.slide .photo{width:100%;height:100%}
.caption{position:absolute;left:0;bottom:0;width:100%;height:88px;background:rgba(225,225,225,.45);padding:29px 0 0 17px}
.caption h3{font-weight:400;font-size:15px;color:#111}
.caption p{font-size:10.5px;color:#222}
.band{left:251px;width:655px;height:101px;display:flex}
.band-green{top:488px;background:var(--lime)}
.band-orange{top:883px;background:var(--orange)}
.cta{color:var(--white);text-align:center;font-size:13px;line-height:15px;text-transform:none}
.cta span{display:block;color:#333}
.band-green .cta{width:109px;padding-top:34px}
.band-green .cta span{color:var(--ink)}
.band-orange .cta{width:106px;padding-top:34px}
.band .shot{height:101px}
.slogan{font-size:27px;color:#3a3a3a;flex:1;text-align:center;padding-top:33px}
.section-title{left:0;width:1164px;top:618px;text-align:center;font-size:17px;color:var(--muted);font-weight:400}
.bio{left:276px;top:661px;width:612px;text-align:center;font-size:11.2px;line-height:19.6px;color:#444}
.mail{left:445px;top:853px;width:268px;height:30px;background:var(--tab);border-radius:4px 4px 0 0;color:var(--white);font-size:11px;text-align:center;line-height:30px}
.footer{left:0;top:983px;width:1200px;height:216px;background:var(--black)}
.testimonial-title{left:0;width:1164px;top:1023px;text-align:center;font-size:19px;color:#333;font-weight:400}
.quote{left:376px;top:1061px;width:456px;text-align:center;font-size:10.5px;line-height:13px;color:var(--white)}
.quote em{font-style:normal;color:var(--lime)}
.view-all{left:0;width:1166px;top:1109px;text-align:center;font-size:9.5px;color:#555;font-style:italic;text-decoration:underline}
.rule{left:251px;top:1140px;width:655px;height:1px;background:#1e1e1e}
.footer-logo{left:252px;top:1160px;font-size:20px;color:var(--white)}
.footer-links{left:346px;top:1161px;font-size:6.5px;color:#666;line-height:11px}
</style>
</head>
<body>
<header class="abs masthead"></header>
<div class="abs lens" role="img" aria-label="Close-up photograph of a camera lens"></div>
<div class="abs logo">corVenna</div>
<nav class="abs nav">
  <a class="current" href="#">Gallery</a>
  <a class="s" href="#">Services</a>
  <a class="a" href="#">About Me</a>
  <a class="t" href="#">Testimonial</a>
  <a class="f" href="#">FAQ</a>
  <a class="c" href="#">Client Login</a>
</nav>
<h1 class="abs tagline" style="font-weight:400">Portrait Photographer<br>Sydney Australia</h1>

<div class="abs photo side-left" role="img" aria-label="Black and white portrait, previous slide"></div>
<div class="abs photo side-right" role="img" aria-label="Black and white portrait, next slide"></div>
<div class="abs slide">
  <div class="photo" role="img" aria-label="Black and white portrait of a woman by a window"></div>
  <div class="caption"><h3>Lorem ipsum dolor sit amet</h3><p>consectetur adipisicing elit</p></div>
</div>

<section class="abs band band-green">
  <div class="cta">+view<span>GALLERY</span></div>
  <div class="shot photo" style="width:79px" role="img" aria-label="Black and white photo of a child"></div>
  <div style="width:6px"></div>
  <div class="shot" style="width:172px;background:linear-gradient(135deg,#4d3a2c,#8a6a4c 50%,#6d7f96)" role="img" aria-label="Photo of two toddlers on a wooden chair"></div>
  <div class="slogan">Relive the moment</div>
</section>

<h2 class="abs section-title">ABOUT ME</h2>
<p class="abs bio">Located on the Lower North Shore in Sydney, Australia, I have been photographing professionally for over seven years.<br>At first I combined graphic design with photography and produced personalised wedding stationery and greeting<br>cards. Later, with the birth of my daughter Mira, I developed a natural interest in pregnancy and babies.<br>I shot a lot of pregnant bellies and their resulting miracles and was hooked.<br>Being a mum of two small children helps me relate and bond with all of my "star models". I've learned many tricks on<br>how to relate to them and keep it relaxed and fun from experimenting with my own children.<br>I am privileged to be able to do what I love most: capturing a moment and transforming it into an everlasting story.</p>

<div class="abs mail">Mail Me :&nbsp; corvenna@corvenna.com.au</div>
<section class="abs band band-orange">
  <div class="slogan" style="flex:0 0 289px;padding-left:20px">Own the moment</div>
  <div class="shot photo" style="width:173px" role="img" aria-label="Black and white photo of three young children"></div>
  <div style="width:8px"></div>
  <div class="shot photo" style="width:79px" role="img" aria-label="Black and white photo of a child"></div>
  <div class="cta">+video<span>GALLERY</span></div>
</section>

<footer class="abs footer"></footer>
<h2 class="abs testimonial-title">TESTIMONIAL</h2>
<p class="abs quote">My kids had such fun during the photo session. corVenna is great at making the children relax and capturing their best looks." <em>- Harriet L</em></p>
<a class="abs view-all" href="#">view all &gt;&gt;</a>
<div class="abs rule"></div>
<div class="abs footer-logo">corVenna</div>
<div class="abs footer-links">Home &nbsp;|&nbsp; Gallery &nbsp;|&nbsp; Services &nbsp;|&nbsp; About Me &nbsp;|&nbsp; Testimonial &nbsp;|&nbsp; FAQ &nbsp;|&nbsp; Client Login<br>All Rights Reserved 2014 corVenna Bright Studio.</div>
</body>
</html>
```